Red design in a sea of blue ocean

We need a new vehicle wrap that will stand out and will be noticed over all other contractors wraps . Bright coloring easy to ready name, number and services. Attached are some stand out designs to draw insight from.

++Our business card design is also uploaded. Fee free to take inspiration from the card design swapping colors.

Company: Dralto Power Max +
Services : residential Service, Commercial Service New Construction
Smart Homes, Solar, LED lighting,

Additional Partnered Services :
Hvac, Plumbing, Window Cleaning Christmas alighting, Home and Vacation Rental cleaning, car detailing

Please make designs on

Brenvik t 270 with a utility shell
Brenvik cargo high roof
Brenvik cargo link

Target Market(s)

Home owners

Industry/Entity Type

Electric Company

Requirements
Must have
• Name, logo, services and phone number

```html
<!DOCTYPE html>
<html lang="en">
<head>
<meta charset="utf-8">
<title>Dralto Power Max + — Fleet Wrap</title>
<link href="https://fonts.googleapis.com/css2?family=Ubuntu:wght@500;700&display=swap" rel="stylesheet">
<style>
  :root{
    --wrap-green:#8dc63f;
    --wrap-black:#1c1a1b;
    --wrap-blue:#1f76bf;
    --tire:#111;
    --rim:#b9bcc0;
    --glass:#2a2d31;
    --light-red:#b8232a;
    --chrome:#d9dadb;
    --shadow:#1a1a1a;
    --white:#ffffff;
    --page:#ffffff;
  }
  html,body{margin:0;padding:0;width:1200px;height:1095px;overflow:hidden;background:var(--page);}
  .fleet{display:block;width:1200px;height:1095px;}
  .service{font-family:"Ubuntu",sans-serif;font-weight:700;fill:var(--white);}
  .bullet{fill:var(--wrap-blue);}
  .brand-name{font-family:"Ubuntu",sans-serif;font-weight:700;fill:var(--wrap-blue);}
  .body-black{fill:var(--wrap-black);}
  .band-green{fill:var(--wrap-green);}
  .stripe-blue{fill:var(--wrap-blue);}
  .tire{fill:var(--tire);}
  .rim{fill:var(--rim);}
  .glass{fill:var(--glass);}
  .tail-light{fill:var(--light-red);}
  .head-light{fill:var(--chrome);}
  .bumper{fill:var(--chrome);}
  .brand-dot{fill:var(--wrap-green);}
</style>
</head>
<body>
<svg class="fleet" viewBox="0 0 2000 1825" xmlns="http://www.w3.org/2000/svg">

  <!-- Cargo high roof van -->
  <g class="vehicle vehicle--van">
    <ellipse cx="1000" cy="890" rx="830" ry="30" fill="#cfcfcf"/>
    <path class="body-black" d="M150 720 L160 650 L190 590 Q240 555 380 520 L620 320 Q700 225 940 155 L1780 143 Q1800 150 1802 200 L1810 500 L1820 700 L1838 800 L1610 805 Q1590 700 1515 700 Q1420 700 1400 805 L535 815 Q520 720 425 720 Q330 720 310 830 L152 820 Z"/>
    <path class="band-green" d="M760 215 Q850 168 950 155 L1780 143 Q1798 150 1800 200 L1798 282 Q1300 300 1000 276 Q850 258 760 215 Z"/>
    <path class="stripe-blue" d="M1240 302 Q1520 295 1800 283 L1800 296 Q1520 310 1240 306 Z"/>
    <path class="stripe-blue" d="M178 612 Q480 580 780 598 L780 604 Q480 594 176 628 Z"/>
    <path class="band-green" d="M176 628 Q480 594 780 604 Q1100 640 1270 692 L560 705 L290 705 Q210 705 165 712 L170 660 Z"/>
    <rect x="150" y="705" width="1250" height="62" class="body-black"/>
    <path class="band-green" d="M570 768 L1380 760 L1372 800 L570 810 Z"/>
    <path class="glass" role="img" aria-label="Van cab side window" d="M495 505 L625 375 L760 345 L760 510 Q700 530 620 548 Z"/>
    <path class="head-light" role="img" aria-label="Headlamp" d="M200 600 L330 565 L270 636 L198 640 Z"/>
    <rect class="tail-light" x="1778" y="510" width="38" height="175" rx="8" role="img" aria-label="Tail lamp"/>
    <g class="wheel">
      <circle cx="425" cy="825" r="100" class="tire"/>
      <circle cx="425" cy="825" r="64" class="rim" role="img" aria-label="Front wheel rim"/>
    </g>
    <g class="wheel">
      <circle cx="1515" cy="825" r="100" class="tire"/>
      <circle cx="1515" cy="825" r="64" class="rim" role="img" aria-label="Rear wheel rim"/>
    </g>

    <g class="services services--roof">
      <circle class="bullet" cx="865" cy="205" r="8"/>
      <text class="service" x="888" y="222" font-size="56">Residential Service</text>
      <circle class="bullet" cx="1434" cy="204" r="5"/>
      <text class="service" x="1450" y="214" font-size="31">Commercial Service</text>
      <circle class="bullet" cx="1084" cy="261" r="4"/>
      <text class="service" x="1097" y="269" font-size="27">New Construction</text>
      <circle class="bullet" cx="1350" cy="261" r="8"/>
      <text class="service" x="1378" y="278" font-size="56">Smart Homes</text>
    </g>
    <g class="services services--lower">
      <circle class="bullet" cx="566" cy="667" r="9"/>
      <text class="service" x="594" y="684" font-size="58">Solar</text>
      <circle class="bullet" cx="774" cy="664" r="5"/>
      <text class="service" x="792" y="675" font-size="38">LED lighting</text>
    </g>
    <g class="brand">
      <circle class="brand-dot" cx="1028" cy="460" r="125"/>
      <text class="brand-name" x="1200" y="500" font-size="150">Dralto</text>
      <text class="brand-name" x="1200" y="610" font-size="86">Power Max +</text>
    </g>
  </g>

  <!-- Pickup with utility shell -->
  <g class="vehicle vehicle--truck">
    <path d="M300 1545 Q230 1580 300 1610 Q700 1660 1200 1640 Q1700 1635 1790 1600 Q1840 1560 1720 1520 Z" fill="var(--shadow)"/>
    <path class="body-black" d="M250 1480 L262 1340 L280 1278 Q420 1245 590 1225 L760 1105 Q960 1082 1230 1080 L1700 1080 Q1760 1140 1805 1225 L1808 1430 L1830 1480 L1600 1490 Q1580 1410 1480 1410 Q1380 1410 1360 1495 L560 1500 Q540 1395 440 1395 Q340 1395 320 1480 Z"/>
    <path class="stripe-blue" d="M265 1332 Q560 1305 830 1322 L830 1327 Q560 1318 262 1348 Z"/>
    <path class="band-green" d="M262 1348 Q560 1318 830 1327 Q1150 1350 1350 1420 L1560 1420 Q1700 1430 1820 1410 L1825 1470 L1610 1485 Q1585 1410 1480 1410 Q1380 1410 1355 1498 L575 1500 Q545 1390 440 1390 Q330 1390 305 1480 L250 1470 Z"/>
    <path class="glass" role="img" aria-label="Truck cab windows" d="M612 1255 L760 1120 L1170 1108 L1185 1250 Q900 1258 612 1268 Z"/>
    <path class="tail-light" role="img" aria-label="Tail lamp" d="M1740 1275 L1805 1270 L1805 1360 L1760 1355 Q1725 1320 1740 1275 Z"/>
    <path class="bumper" role="img" aria-label="Front bumper" d="M250 1425 L290 1420 L300 1475 L252 1470 Z"/>
    <path class="bumper" role="img" aria-label="Rear bumper" d="M1745 1425 L1830 1420 L1832 1475 L1765 1478 Z"/>
    <rect x="590" y="1502" width="600" height="14" fill="#3a3a3a"/>
    <g class="wheel">
      <circle cx="440" cy="1520" r="110" class="tire"/>
      <circle cx="440" cy="1520" r="70" class="rim" role="img" aria-label="Front wheel rim"/>
    </g>
    <g class="wheel">
      <circle cx="1480" cy="1525" r="110" class="tire"/>
      <circle cx="1480" cy="1525" r="70" class="rim" role="img" aria-label="Rear wheel rim"/>
    </g>

    <g class="services services--side">
      <circle class="bullet" cx="577" cy="1373" r="7"/>
      <text class="service" x="598" y="1385" font-size="44">Solar</text>
      <circle class="bullet" cx="732" cy="1370" r="4"/>
      <text class="service" x="745" y="1379" font-size="30">LED lighting</text>
      <circle class="bullet" cx="606" cy="1415" r="5"/>
      <text class="service" x="622" y="1426" font-size="32">Residential Service</text>
      <circle class="bullet" cx="939" cy="1415" r="3"/>
      <text class="service" x="948" y="1421" font-size="19">Commercial Service</text>
      <circle class="bullet" cx="627" cy="1459" r="3"/>
      <text class="service" x="635" y="1465" font-size="18">New Construction</text>
      <circle class="bullet" cx="804" cy="1459" r="5"/>
      <text class="service" x="823" y="1471" font-size="38">Smart Homes</text>
    </g>
    <g class="brand">
      <circle class="brand-dot" cx="1158" cy="1215" r="103"/>
      <text class="brand-name" x="1290" y="1260" font-size="118">Dralto</text>
      <text class="brand-name" x="1290" y="1340" font-size="66">Power Max +</text>
    </g>
  </g>
</svg>
</body>
</html>
```